VORLEN Website Design

We need a website designed for our company VORLEN. We are a luxury lifestyle club that will provide benefits and services for our members. The site should be clean & sleek, preferably using black and white (or darker colors). (example sites: brimvale.example, tusko.example)

Here is a link of a sample page I did using wix. (https://pelmundry4.sitebuild.example/mypage) This can be used to get a general idea.

Target Market(s)

Upper Middle Class in the United States

Number of Pages Required

5+ page

Font styles to use
Sans Serif
Other font styles liked:
• Arial (or other similar fonts)

Requirements
Must have
• A clean design that is eye-catching and speaks to our company.
Nice to have
• Ideas for copy.

```html
<!DOCTYPE html>
<html lang="en">
<head>
<meta charset="utf-8">
<title>VORLEN — A Members Only Lifestyle Club</title>
<link href="https://fonts.googleapis.com/css2?family=Arimo:wght@400;700&display=swap" rel="stylesheet">
<style>
:root{
  --navy:#0c1e44;
  --ink:#0d1a38;
  --teal:#bbe8ea;
  --white:#ffffff;
  --grey:#6b6f78;
  --black:#111111;
}
*{box-sizing:border-box;margin:0;padding:0}
html,body{width:1200px;height:4009px;overflow:hidden}
body{position:relative;background:var(--white);font-family:"Arimo",Arial,sans-serif;color:var(--ink)}
.abs{position:absolute}

/* header */
.site-header{position:absolute;left:0;top:0;width:1200px;height:80px;background:var(--navy);z-index:3}
.brand-tab{position:absolute;left:0;top:0}
.brand{position:absolute;left:32px;top:22px;font-weight:700;font-size:34px;letter-spacing:12px;color:var(--navy)}
.main-nav{position:absolute;top:33px;left:313px;font-size:13px;color:var(--white);white-space:nowrap}
.main-nav span{position:absolute;white-space:nowrap}
.main-nav .sep{opacity:.8}
.tel{position:absolute;left:968px;top:33px;font-size:12px;color:var(--white)}

/* hero */
.hero{position:absolute;left:0;top:0;width:1200px;height:690px;background:linear-gradient(120deg,#2a2f3a 0%,#51525a 35%,#6d6458 55%,#3a3c42 80%,#1f2228 100%)}
.hero-cut{position:absolute;left:0;top:615px;width:869px;height:80px;background:var(--white)}
.hero-title{position:absolute;left:0;top:212px;width:1200px;text-align:center;font-weight:700;font-size:56px;line-height:74px;color:var(--white);letter-spacing:2px;padding-right:10px}

/* services */
.service{position:absolute;height:362px}
.service-photo{position:absolute;top:0;height:362px;width:551px}
.service-panel{position:absolute;top:0;height:362px;background:var(--teal);border-bottom:8px solid var(--navy)}
.service-tag{position:absolute;font-size:16px;font-weight:700;color:var(--ink);white-space:nowrap}
.service-tag::before{content:"";display:inline-block;width:9px;height:9px;background:var(--navy);margin-right:12px;vertical-align:1px}
.service-title{position:absolute;font-size:28px;font-weight:700;letter-spacing:2px;color:var(--ink);white-space:nowrap}
.btn-details{position:absolute;width:134px;height:35px;background:var(--navy);color:var(--white);font-size:11px;font-weight:700;letter-spacing:.5px;display:flex;align-items:center;justify-content:center}

/* covered band */
.covered{position:absolute;left:0;top:2686px;width:1200px;height:187px;background:var(--navy);color:var(--white);text-align:center}
.covered h2{margin-top:42px;font-size:33px;letter-spacing:1.5px}
.covered p{margin:18px auto 0;width:1010px;font-size:12.5px;line-height:24px}

/* about */
.about{position:absolute;left:0;top:2925px;width:1200px;text-align:center}
.about h2{font-size:34px;letter-spacing:2px;color:var(--ink)}
.about p{margin:20px auto 0;width:900px;font-size:12.5px;line-height:24px;color:var(--grey)}

/* contact */
.contact{position:absolute;left:0;top:3194px;width:1200px;height:548px;background:var(--black)}
.contact-photo{position:absolute;left:641px;top:0;width:559px;height:548px;background:radial-gradient(circle at 70% 60%,#6a6a6a 0%,#2e2e2e 40%,#111 80%)}
.contact h2{position:absolute;left:101px;top:54px;font-size:34px;color:var(--white);letter-spacing:1px}
.contact .lead{position:absolute;left:101px;top:112px;font-size:14px;color:var(--white)}
.field{position:absolute;left:102px;width:330px;color:var(--white);font-size:13px}
.field .line{position:absolute;left:77px;width:253px;border-bottom:1px solid #cfcfcf}
.btn-send{position:absolute;left:179px;top:436px;width:176px;height:44px;border:1.5px solid var(--white);color:var(--white);font-size:14px;display:flex;align-items:center;justify-content:center}

/* footer */
.site-footer{position:absolute;left:0;top:3742px;width:1200px;height:267px;background:var(--teal);color:var(--ink)}
.footer-brand{position:absolute;left:100px;top:74px;font-size:24px;font-weight:700;letter-spacing:9px}
.follow{position:absolute;left:104px;top:124px;width:148px;text-align:center;font-size:13px}
.socials{position:absolute;left:102px;top:152px;display:flex;gap:10px}
.socials span{width:31px;height:31px;border-radius:50%;background:var(--navy)}
.copy{position:absolute;left:104px;top:210px;width:148px;text-align:center;font-size:12px}
.f-col{position:absolute;top:50px;font-size:13px}
.f-col h4{font-size:14px;font-weight:700;margin-bottom:22px}
.f-col.light h4{font-weight:400}
.f-col li{list-style:none;line-height:25px}
.f-col .u{text-decoration:underline}
.icon-row{display:flex;align-items:flex-start;gap:10px}
</style>
</head>
<body>

<section class="hero" role="img" aria-label="Photo of business people meeting around a table with a laptop"></section>
<div class="hero-cut"></div>
<h1 class="hero-title">A MEMBERS ONLY<br>LIFESTYLE CLUB</h1>

<header class="site-header">
  <svg class="brand-tab" width="270" height="80" viewBox="0 0 270 80"><polygon points="0,0 270,0 232,80 0,80" fill="#ffffff"/></svg>
  <div class="brand">VORLEN</div>
  <nav class="main-nav">
    <span style="left:0">HOME</span>
    <span class="sep" style="left:52px">//</span>
    <span style="left:85px">SERVICES &amp; BENEFITS</span>
    <span class="sep" style="left:230px">//</span>
    <span style="left:259px">OUR CLIENTS</span>
    <span class="sep" style="left:350px">//</span>
    <span style="left:382px">ABOUT US</span>
    <span class="sep" style="left:455px">//</span>
    <span style="left:484px">CONTACT US</span>
  </nav>
  <div class="tel">TEL: +99 1800 555 0144</div>
</header>

<!-- service 1 -->
<section class="service" style="left:99px;top:650px;width:733px">
  <div class="service-photo" role="img" aria-label="Photo of hands typing on a laptop showing financial spreadsheets" style="left:0;background:linear-gradient(135deg,#2f5c8c 0%,#dde2e8 45%,#f4f4f2 70%,#c9c2b6 100%)"></div>
  <div class="service-panel" style="left:551px;width:182px"></div>
  <div class="service-tag" style="left:583px;top:123px">Service</div>
  <div class="service-title" style="left:579px;top:155px">ACCOUNTING SERVICES</div>
  <div class="btn-details" style="left:580px;top:205px">VIEW DETAILS</div>
</section>

<!-- service 2 -->
<section class="service" style="left:339px;top:1053px;width:765px">
  <div class="service-panel" style="left:0;width:214px"></div>
  <div class="service-photo" role="img" aria-label="Photo of hands reviewing investment charts on a desk with coffee and laptop" style="left:214px;background:linear-gradient(135deg,#3a2a1e 0%,#7b5a3e 35%,#e9e6e1 65%,#6d5440 100%)"></div>
  <div class="service-tag" style="left:104px;top:108px">Service</div>
  <div class="service-title" style="left:-137px;top:156px">INVESTMENT SERVICES</div>
  <div class="btn-details" style="left:56px;top:212px">VIEW DETAILS</div>
</section>

<!-- service 3 -->
<section class="service" style="left:99px;top:1457px;width:733px">
  <div class="service-photo" role="img" aria-label="Photo of shelves of leather-bound law books" style="left:0;background:linear-gradient(180deg,#3b2a22 0%,#7a4a34 40%,#2a2520 55%,#c9c0b0 75%,#3a342e 100%)"></div>
  <div class="service-panel" style="left:551px;width:182px"></div>
  <div class="service-tag" style="left:583px;top:123px">Service</div>
  <div class="service-title" style="left:579px;top:155px">LAWYER SERVICES</div>
  <div class="btn-details" style="left:580px;top:205px">VIEW DETAILS</div>
</section>

<!-- service 4 -->
<section class="service" style="left:339px;top:1858px;width:765px">
  <div class="service-panel" style="left:0;width:214px"></div>
  <div class="service-photo" role="img" aria-label="Photo of a person in a suit working at a desk with a laptop and phone" style="left:214px;background:linear-gradient(135deg,#d8d8d8 0%,#2a2a2a 35%,#111 60%,#e6e6e6 100%)"></div>
  <div class="service-tag" style="left:104px;top:108px">Service</div>
  <div class="service-title" style="left:-137px;top:156px">REAL ESTATE SERVICES</div>
  <div class="btn-details" style="left:56px;top:212px">VIEW DETAILS</div>
</section>

<!-- service 5 -->
<section class="service" style="left:99px;top:2272px;width:733px">
  <div class="service-photo" role="img" aria-label="Photo of guests in masquerade masks at an evening party" style="left:0;background:linear-gradient(135deg,#c2203a 0%,#7a1f5c 40%,#2b2a6b 75%,#151a45 100%)"></div>
  <div class="service-panel" style="left:551px;width:182px"></div>
  <div class="service-tag" style="left:583px;top:142px">Service</div>
  <div class="service-title" style="left:579px;top:180px">EVENT ACCESS</div>
  <div class="btn-details" style="left:580px;top:240px">VIEW DETAILS</div>
</section>

<section class="covered">
  <h2>WE'VE GOT YOU COVERED</h2>
  <p>Glittering awards, brilliant branding events, state of the art exhibitions, we can handle them all and more. Let your hair down or showcase your stature — no matter what sort of experience you require, we can make sure it leaves a vivid impression.</p>
</section>

<section class="about">
  <h2>ABOUT VORLEN</h2>
  <p>Built in the image of a "Multi-Family Office", VORLEN provides members with access to just about any service, experience, and event desirable.<br>VORLEN is truly the most exclusive lifestyle club out there.</p>
</section>

<section class="contact">
  <div class="contact-photo" role="img" aria-label="Black and white photo of a band performing on stage under a spotlight"></div>
  <h2>CONTACT US</h2>
  <div class="lead">We're always here, drop us a line!</div>
  <div class="field" style="top:160px">Name<span class="line" style="top:16px"></span></div>
  <div class="field" style="top:216px">Email<span class="line" style="top:16px"></span></div>
  <div class="field" style="top:275px">Phone<span class="line" style="top:16px"></span></div>
  <div class="field" style="top:331px">Message<span class="line" style="top:62px"></span></div>
  <div class="btn-send">Send Message</div>
</section>

<footer class="site-footer">
  <div class="footer-brand">VORLEN</div>
  <div class="follow">Follow us on</div>
  <div class="socials"><span></span><span></span><span></span><span></span></div>
  <div class="copy">© 2018 VORLEN.</div>

  <div class="f-col" style="left:385px">
    <h4>SERVICES</h4>
    <ul><li>Event Management</li><li>Investment Services</li><li>Accounting Services</li><li>Event Production</li></ul>
  </div>
  <div class="f-col light" style="left:639px">
    <h4>QUICK LINKS</h4>
    <ul><li>Apply NOw</li><li>Contact us</li></ul>
  </div>
  <div class="f-col light" style="left:863px">
    <h4>GET IN TOUCH</h4>
    <ul>
      <li class="icon-row"><svg width="12" height="14" viewBox="0 0 24 24" style="margin-top:6px"><path d="M6.6 10.8a15 15 0 0 0 6.6 6.6l2.2-2.2a1 1 0 0 1 1-.25 11.4 11.4 0 0 0 3.6.57 1 1 0 0 1 1 1V20a1 1 0 0 1-1 1A17 17 0 0 1 3 4a1 1 0 0 1 1-1h3.5a1 1 0 0 1 1 1c0 1.25.2 2.45.57 3.6a1 1 0 0 1-.25 1z" fill="#0d1a38"/></svg><span>1800-555-0199</span></li>
      <li class="icon-row"><svg width="12" height="14" viewBox="0 0 24 24" style="margin-top:6px"><path d="M12 2a7 7 0 0 0-7 7c0 5.2 7 13 7 13s7-7.8 7-13a7 7 0 0 0-7-7zm0 9.5A2.5 2.5 0 1 1 12 6.5a2.5 2.5 0 0 1 0 5z" fill="#0d1a38"/></svg><span><span class="u">Find on map</span><br>304, Lorem Ipsaum<br>Business Centre, Halden Estate,<br>Marlow, Kentshire KT4 2PL</span></li>
    </ul>
  </div>
</footer>

</body>
</html>
```